Poster for a new "Pizza Roll" Combo at our bakery

We are a cinnamon roll and coffee focused bakery, but we would like an innovative poster design to bring attention to our new offering, a Pizza Roll. We will be offering it as a combo, and this is what we wish to advertise. It will be geared mainly towards a younger high school aged crowd. I have included pics of the Pizza Rolls, but it's up to you how you want to incorporate them in the design.Poster should include our logo, the pizza rolls, and can include a drink to illustrate the combo as well. ( we offer710 ml vima bottle products and lurn bottled waters)Main Text: Try our amazing new Pizza Rolls! Message to get accross: $6.00 for a Pizza Roll and drink.Small Print: Avail after 11am, while supplies last. Includes one pizza roll and one bottled drink of choice. Taxes extra.

Target Market(s)

Broad, but mainly high school aged kids

Industry/Entity Type

Bakery

Colors

Designer to choose colors to be used in the design.

Requirements
Must have
• Text: " Try our amazing new PIzza Rolls!:
• $6 Pizza Roll Combo (Pizza Roll and a drink)
Nice to have
• Pic of the PIzza Roll (photo shopped if needed to improve esthetics)
• Pic of a Bottled 710ml vima drink
Should not have
• Any animal product references, as we are a Vegan shop.

```html
<!DOCTYPE html>
<html lang="en">
<head>
<meta charset="utf-8">
<title>Pizza Roll Combo Poster</title>
<link rel="stylesheet" href="https://fonts.googleapis.com/css2?family=Almendra:wght@700&family=Archivo+Black&family=Arimo:wght@400;700&display=swap">
<style>
  :root {
    --page: #ffffff;
    --bokeh-light: #c9a27e;
    --bokeh-mid: #a9805f;
    --bokeh-dark: #7d5a45;
    --wood-light: #c89c74;
    --wood-dark: #9b7252;
    --burst-red: #e81c24;
    --burst-edge: #ffffff;
    --new-yellow: #ffd400;
    --offer-red: rgba(205, 45, 30, 0.85);
    --roll-gold: #e2a64a;
    --roll-crust: #f2d39a;
    --cola-dark: #2a1714;
    --label-red: #d4111b;
    --water-blue: #d7e9f4;
    --cap-blue: #1e3f7a;
    --white: #ffffff;
  }
  * { margin: 0; padding: 0; box-sizing: border-box; }
  html, body { width: 1200px; height: 1200px; overflow: hidden; background: var(--page); }
  .poster {
    position: absolute; left: 221px; top: 30px; width: 759px; height: 1140px;
    overflow: hidden;
  }
  .backdrop {
    position: absolute; inset: 0 0 342px 0;
    background:
      radial-gradient(circle at 85% 20%, rgba(255,235,200,.55) 0 40px, transparent 80px),
      radial-gradient(circle at 10% 60%, rgba(255,220,200,.35) 0 60px, transparent 140px),
      linear-gradient(180deg, var(--bokeh-mid), var(--bokeh-light) 55%, var(--bokeh-dark));
  }
  .table {
    position: absolute; left: 0; right: 0; bottom: 0; height: 342px;
    background: linear-gradient(180deg, var(--wood-light), var(--wood-dark));
  }
  .headline {
    position: absolute; top: 26px; left: 0; width: 100%;
    text-align: center; color: var(--white);
    font-family: "Almendra", Georgia, serif; font-weight: 700; font-size: 72px; line-height: 1.1;
    transform: rotate(-2deg);
    text-shadow: 0 2px 4px rgba(0,0,0,.25);
  }
  .burst { position: absolute; left: -2px; top: 98px; width: 524px; height: 448px; transform: rotate(-6deg); }
  .new-word {
    position: absolute; left: 255px; top: 320px;
    transform: translate(-50%, -50%) rotate(-15deg);
    font-family: "Archivo Black", Arial, sans-serif; font-size: 140px; line-height: 1;
    color: var(--new-yellow); text-shadow: 3px 4px 4px rgba(0,0,0,.35);
  }
  .bottle { position: absolute; border-radius: 40px 40px 18px 18px; }
  .bottle-cola { left: 491px; top: 382px; width: 120px; height: 432px; background: var(--cola-dark); }
  .bottle-water { left: 618px; top: 384px; width: 121px; height: 432px; background: var(--water-blue); }
  .bottle-cap { position: absolute; left: 35px; top: -2px; width: 50px; height: 34px; border-radius: 6px; }
  .bottle-cola .bottle-cap { background: var(--label-red); }
  .bottle-water .bottle-cap { background: var(--cap-blue); }
  .bottle-label {
    position: absolute; left: 0; width: 100%; text-align: center;
    font-family: "Arimo", Arial, sans-serif; font-weight: 700; font-size: 30px;
  }
  .bottle-cola .bottle-label { top: 176px; padding: 12px 0; background: var(--label-red); color: var(--white); }
  .bottle-water .bottle-label { top: 296px; color: var(--cap-blue); }
  .product-name {
    position: absolute; left: 262px; top: 592px; z-index: 2;
    transform: translate(-50%, -50%) rotate(-22deg);
    font-family: "Almendra", Georgia, serif; font-weight: 700; font-size: 92px; line-height: 1;
    color: var(--white); white-space: nowrap; text-shadow: 0 2px 5px rgba(0,0,0,.3);
  }
  .roll-photo {
    position: absolute; left: 31px; top: 758px; width: 416px; height: 296px;
    border-radius: 48% 48% 40% 40% / 40% 40% 55% 55%;
    background: radial-gradient(ellipse at 50% 35%, var(--roll-gold), var(--roll-crust) 75%);
  }
  .offer { position: absolute; left: 393px; top: 704px; width: 364px; height: 364px; z-index: 3; }
  .offer-text {
    position: absolute; left: 585px; top: 766px; transform: translateX(-50%); z-index: 4;
    text-align: center; color: var(--white); font-family: "Arimo", Arial, sans-serif;
    white-space: nowrap;
  }
  .offer-price { font-size: 86px; line-height: 96px; font-weight: 700; }
  .offer-items { font-size: 54px; line-height: 62px; font-weight: 400; }
  .small-print {
    position: absolute; left: 0; bottom: 16px; width: 100%; text-align: center;
    color: var(--white); font-family: "Arimo", Arial, sans-serif; font-size: 14px;
  }
</style>
</head>
<body>
  <main class="poster">
    <div class="backdrop" role="img" aria-label="Blurred warm bakery interior with soft lights"></div>
    <div class="table" role="img" aria-label="Wooden table top"></div>

    <h1 class="headline">Try out our amazing</h1>

    <svg class="burst" viewBox="0 0 524 448" aria-hidden="true">
      <polygon fill="var(--burst-red)" stroke="var(--burst-edge)" stroke-width="6" stroke-linejoin="miter"
        points="517,224 434,249 502,298 414,297 457,362 375,335 390,410 322,360 306,436 262,369 218,436 202,360 134,410 149,335 67,362 110,297 22,298 90,249 7,224 90,199 22,150 110,151 67,86 149,113 134,38 202,88 218,12 262,79 306,12 322,88 390,38 375,113 457,86 414,151 502,150 434,199"/>
    </svg>
    <div class="new-word">NEW</div>

    <div class="bottle bottle-cola" role="img" aria-label="Photo of a bottle of vima cola">
      <span class="bottle-cap"></span>
      <span class="bottle-label">vima</span>
    </div>
    <div class="bottle bottle-water" role="img" aria-label="Photo of a bottle of lurn water">
      <span class="bottle-cap"></span>
      <span class="bottle-label">lurn</span>
    </div>

    <h2 class="product-name">Pizza Rolls</h2>

    <div class="roll-photo" role="img" aria-label="Photo of a golden baked pizza roll"></div>

    <svg class="offer" viewBox="0 0 364 364" aria-hidden="true">
      <circle cx="182" cy="182" r="182" fill="var(--offer-red)"/>
    </svg>
    <div class="offer-text">
      <div class="offer-price">$6.00</div>
      <div class="offer-items">Pizza Roll<br>&amp;<br>Drink</div>
    </div>

    <p class="small-print">Avail after 11am, while supplies last. Includes one pizza roll and one bottled drink of choice. Taxes extra.</p>
  </main>
</body>
</html>
```